Stationary for New Company

We need stationary designed for a new company. Details of the required stationary is attached.

The final version should be trendy, clean... only 2 colours (green + grey/black) and professional.

#1: Business Cards (design on 2 sides)
#2: Letterhead (word format)
#3: Cover Page and back cover for proposals
#4: Envelopes,
#5: Thank You card,
#6: Presentation Folder,
#7: Email signatures template (sample attached in word document)

Logo is attached. Logo can be reversed out (will attach once available). Logo can be stacked or horizontal (provided as horizontal).

Files need to be provided in ai + png format.

Target Market(s)

Business owners. More affluent.

Industry/Entity Type

Business

Requirements
Must have
• See brief

Font: Calibri
Should not have
• Photographs / stock photos

```html
<!DOCTYPE html>
<html lang="en">
<head>
<meta charset="utf-8">
<title>Northgate Insurance Brokers – Stationery</title>
<link rel="stylesheet" href="https://fonts.googleapis.com/css2?family=Carlito:wght@400;700&family=Great+Vibes&display=swap">
<style>
:root{
  --green:#5e8c36;
  --green-dark:#4f7a2c;
  --ink:#2b2b2b;
  --grey:#7a7a7a;
  --rule:#bdbdbd;
  --paper:#ffffff;
  --stage:#c3c3c3;
}
*{box-sizing:border-box;margin:0;padding:0}
html,body{width:1200px;height:640px;overflow:hidden}
body{background:var(--stage);font-family:"Carlito","Calibri",sans-serif;color:var(--ink);position:relative}
.piece{position:absolute;background:var(--paper);box-shadow:1px 2px 4px rgba(0,0,0,.35);overflow:hidden}
.icon{width:7px;height:7px;fill:var(--ink);color:var(--ink);vertical-align:-1px;margin-right:4px}
.icon-green{fill:var(--green);color:var(--green)}
.contact{list-style:none;font-size:7px;font-weight:700;line-height:9px;white-space:nowrap}
.contact .gap{margin-top:5px}
.wordmark{display:flex;align-items:center;gap:6px;color:var(--green)}
.wordmark .mark-square{background:var(--green);flex:none}
.wordmark .name{line-height:.95}
.wordmark .name b{display:block;font-weight:400}
.wordmark .name span{display:block;font-weight:400}
.reverse .wordmark{color:#fff}
.reverse .wordmark .mark-square{background:#fff}

/* business cards */
.card{top:14px;width:222px;height:130px}
.card-1{left:16px}.card-2{left:251px}.card-3{left:486px}.card-4{left:721px}.card-5{left:956px;background:var(--green)}
.card .person{color:var(--green);font-weight:700;font-size:11px;line-height:13px}
.card .person small{font-size:6.5px;color:var(--ink)}
.card .role{font-size:6.5px;font-weight:700;line-height:8px}
.card-1 .header{position:absolute;right:10px;top:9px;text-align:right}
.card-1 .header-rule{position:absolute;left:0;right:10px;top:33px;border-top:1px solid var(--rule)}
.card-1 .contact{position:absolute;left:12px;top:50px}
.card-1 .address{color:var(--green)}
.card-1 .band{position:absolute;right:0;bottom:0;width:48px;height:8px;background:var(--green)}
.card-2 .wordmark{position:absolute;right:14px;top:14px}
.card-2 .header{position:absolute;left:12px;top:44px}
.card-2 .header-rule{position:absolute;left:0;right:0;top:66px;border-top:1px solid var(--green)}
.card-2 .contact{position:absolute;top:80px}
.card-2 .col-a{left:12px}
.card-2 .col-b{left:122px;padding-left:5px;border-left:1px solid var(--rule);font-size:6.4px}
.card-2 .col-b .icon{width:6px;height:6px;margin-right:3px}
.card-3 .header{position:absolute;left:12px;top:9px}
.card-3 .contact{position:absolute;left:12px;top:46px}
.card-4 .wordmark,.card-5 .wordmark{position:absolute;left:26px;top:44px}
.wm-card .mark-square{width:30px;height:30px}
.wm-card .name b{font-size:27px}
.wm-card .name span{font-size:10px}

/* letterhead */
.letterhead{left:16px;top:168px;width:352px;height:456px}
.letterhead .wordmark{position:absolute;left:26px;top:28px}
.wm-lh .mark-square{width:26px;height:26px}
.wm-lh .name b{font-size:21px}
.wm-lh .name span{font-size:8px}
.letterhead .address{position:absolute;left:204px;top:36px;color:var(--green);font-size:5.6px;font-weight:700;line-height:7px}
.letterhead .contact{position:absolute;left:262px;top:32px;padding-left:4px;border-left:1px solid var(--rule);font-size:5.2px;line-height:7px}
.letterhead .contact .icon{width:5px;height:5px;margin-right:2px}
.letterhead .contact .gap{margin-top:2px}
.letterhead .footer-band{position:absolute;left:0;right:0;bottom:0;height:10px;background:var(--green)}

/* folder */
.folder{top:176px;height:210px;display:flex}
.folder-outside{left:390px;width:300px}
.folder-inside{left:710px;width:300px}
.panel{flex:1;position:relative}
.panel-green{background:var(--green)}
.folder-inside .panel{background:linear-gradient(180deg,#5a8733,#6b9a41)}
.folder-inside .panel+.panel{border-left:1px solid var(--green-dark)}
.pocket{position:absolute;left:0;right:0;bottom:0;height:62px;background:#f3f3f3;display:flex;align-items:center;justify-content:center}
.wm-small .mark-square{width:12px;height:12px}
.wm-small .name b{font-size:10px}
.wm-small .name span{font-size:4.5px}
.panel-front .wordmark{position:absolute;left:16px;top:14px}
.wm-folder .mark-square{width:17px;height:17px}
.wm-folder .name b{font-size:15px}
.wm-folder .name span{font-size:6px}
.panel-back .wordmark{position:absolute;left:12px;bottom:30px}
.panel-back .micro{position:absolute;left:12px;bottom:12px;color:#fff;font-size:3.8px;line-height:5px;display:flex;gap:8px}

/* thank-you card */
.thanks{left:1030px;top:176px;width:150px;height:210px}
.thanks .script{position:absolute;top:14px;left:0;right:0;text-align:center;font-family:"Great Vibes",cursive;color:var(--green);font-size:20px}
.thanks .wordmark{position:absolute;left:42px;bottom:26px}
.thanks .footer-band{position:absolute;left:0;right:0;bottom:0;height:20px;background:var(--green);color:#fff;font-size:3.9px;line-height:5px;display:flex;justify-content:space-around;align-items:center;padding:0 3px}

/* envelopes */
.envelope{top:424px;width:370px;height:160px}
.envelope-front{left:390px}
.envelope-back{left:780px;background:#fbfbfb}
.envelope-front .wordmark{position:absolute;left:16px;top:18px}
.envelope-front .return{position:absolute;left:42px;top:54px;font-size:5.8px;line-height:7.5px}
.envelope-front .footer-band{position:absolute;left:0;right:0;bottom:0;height:14px;background:var(--green)}
.envelope-back svg.flap{position:absolute;inset:0}
.envelope-back .seal{position:absolute;left:169px;top:22px;width:32px;height:32px;background:var(--green)}
</style>
</head>
<body>
<svg width="0" height="0" style="position:absolute" aria-hidden="true">
  <symbol id="i-phone" viewBox="0 0 10 10"><path d="M2 1h2l1 2.5-1.3 1a6 6 0 0 0 2.8 2.8l1-1.3L10 7v2c0 .6-.4 1-1 1A9 9 0 0 1 0 1c0-.6.4-1 1-1z"/></symbol>
  <symbol id="i-fax" viewBox="0 0 10 10"><rect x="2" y="0" width="6" height="3"/><rect x="0" y="3.5" width="10" height="6.5" rx="1"/></symbol>
  <symbol id="i-mobile" viewBox="0 0 10 10"><rect x="2.5" y="0" width="5" height="10" rx="1"/></symbol>
  <symbol id="i-web" viewBox="0 0 10 10"><circle cx="5" cy="5" r="4.3" fill="none" stroke="currentColor" stroke-width="1.2"/><path d="M.7 5h8.6M5 .7v8.6" stroke="currentColor" stroke-width="1"/></symbol>
  <symbol id="i-mail" viewBox="0 0 10 10"><rect x="0" y="1.5" width="10" height="7" rx="1"/></symbol>
  <symbol id="i-pin" viewBox="0 0 10 10"><path d="M5 0a3.6 3.6 0 0 1 3.6 3.6C8.6 6.5 5 10 5 10S1.4 6.5 1.4 3.6A3.6 3.6 0 0 1 5 0z"/></symbol>
</svg>

<!-- Business card front: full contact -->
<section class="piece card card-1">
  <div class="header"><div class="person">Daniel Reeve, <small>BA, CRM</small></div><div class="role">President &amp; CEO</div></div>
  <div class="header-rule"></div>
  <ul class="contact">
    <li><svg class="icon"><use href="#i-phone"/></svg>780.555.0142</li>
    <li><svg class="icon"><use href="#i-phone"/></svg>780.555.0177 (Direct)</li>
    <li><svg class="icon"><use href="#i-fax"/></svg>780.555.0163</li>
    <li><svg class="icon"><use href="#i-mobile"/></svg>888.555.0190 (Toll Free)</li>
    <li class="gap"><svg class="icon"><use href="#i-web"/></svg>www.northgatecover.com</li>
    <li><svg class="icon"><use href="#i-mail"/></svg>dreeve@northgatecover.com</li>
    <li class="address">2240 Larch Street NW, Calgary, AB T2N 4K8</li>
  </ul>
  <div class="band"></div>
</section>

<!-- Business card: wordmark and two columns -->
<section class="piece card card-2">
  <div class="wordmark wm-small"><div class="mark-square"></div><div class="name"><b>Northgate</b><span>Insurance Brokers</span></div></div>
  <div class="header"><div class="person">Daniel Reeve, <small>BA, CRM</small></div><div class="role">President &amp; CEO</div></div>
  <div class="header-rule"></div>
  <ul class="contact col-a">
    <li><svg class="icon"><use href="#i-phone"/></svg>780.555.0142</li>
    <li><svg class="icon"><use href="#i-phone"/></svg>780.555.0177 (Direct)</li>
    <li><svg class="icon"><use href="#i-fax"/></svg>780.555.0163</li>
    <li><svg class="icon"><use href="#i-mobile"/></svg>888.555.0190 (Toll Free)</li>
  </ul>
  <ul class="contact col-b">
    <li><svg class="icon icon-green"><use href="#i-web"/></svg>www.northgatecover.com</li>
    <li><svg class="icon icon-green"><use href="#i-mail"/></svg>dreeve@northgatecover.com</li>
    <li><svg class="icon icon-green"><use href="#i-pin"/></svg>2240 Larch Street NW</li>
    <li style="padding-left:9px">Calgary, AB T2N 4K8</li>
  </ul>
</section>

<!-- Business card: designation template -->
<section class="piece card card-3">
  <div class="header"><div class="person">Daniel Reeve, <small>BA, CRM</small></div><div class="role">Designation</div></div>
  <ul class="contact">
    <li><svg class="icon"><use href="#i-phone"/></svg>780.555.0142</li>
    <li><svg class="icon"><use href="#i-phone"/></svg>780.555.0177 (Direct)</li>
    <li><svg class="icon"><use href="#i-fax"/></svg>780.555.0163</li>
    <li><svg class="icon"><use href="#i-mobile"/></svg>888.555.0190 (Toll Free)</li>
    <li class="gap"><svg class="icon"><use href="#i-web"/></svg>www.northgatecover.com</li>
    <li><svg class="icon"><use href="#i-mail"/></svg>dreeve@northgatecover.com</li>
    <li><svg class="icon"><use href="#i-pin"/></svg>2240 Larch Street NW, Calgary, AB T2N 4K8</li>
  </ul>
</section>

<!-- Business card backs -->
<section class="piece card card-4">
  <div class="wordmark wm-card"><div class="mark-square"></div><div class="name"><b>Northgate</b><span>Insurance Brokers</span></div></div>
</section>
<section class="piece card card-5 reverse">
  <div class="wordmark wm-card"><div class="mark-square"></div><div class="name"><b>Northgate</b><span>Insurance Brokers</span></div></div>
</section>

<!-- Letterhead -->
<section class="piece letterhead">
  <div class="wordmark wm-lh"><div class="mark-square"></div><div class="name"><b>Northgate</b><span>Insurance Brokers</span></div></div>
  <div class="address">2240 Larch Street NW<br>Calgary, AB T2N 4K8</div>
  <ul class="contact">
    <li><svg class="icon"><use href="#i-phone"/></svg>780.555.0142</li>
    <li><svg class="icon"><use href="#i-fax"/></svg>780.555.0163</li>
    <li class="gap"><svg class="icon"><use href="#i-web"/></svg>www.northgatecover.com</li>
    <li><svg class="icon"><use href="#i-mail"/></svg>dreeve@northgatecover.com</li>
  </ul>
  <div class="footer-band"></div>
</section>

<!-- Presentation folder, outside spread -->
<section class="piece folder folder-outside">
  <div class="panel panel-green panel-back reverse">
    <div class="wordmark wm-small"><div class="mark-square"></div><div class="name"><b>Northgate</b><span>Insurance Brokers</span></div></div>
    <div class="micro"><span>2240 Larch Street NW<br>Calgary, AB T2N 4K8</span><span>780.555.0142<br>780.555.0163</span><span>northgatecover.com<br>dreeve@northgatecover.com</span></div>
  </div>
  <div class="panel panel-front">
    <div class="wordmark wm-folder"><div class="mark-square"></div><div class="name"><b>Northgate</b><span>Insurance Brokers</span></div></div>
  </div>
</section>

<!-- Presentation folder, inside spread -->
<section class="piece folder folder-inside">
  <div class="panel"><div class="pocket"><div class="wordmark wm-small"><div class="mark-square"></div><div class="name"><b>Northgate</b><span>Insurance Brokers</span></div></div></div></div>
  <div class="panel"><div class="pocket"><div class="wordmark wm-small"><div class="mark-square"></div><div class="name"><b>Northgate</b><span>Insurance Brokers</span></div></div></div></div>
</section>

<!-- Thank-you card -->
<section class="piece thanks">
  <div class="script">Thank You</div>
  <div class="wordmark wm-small"><div class="mark-square"></div><div class="name"><b>Northgate</b><span>Insurance Brokers</span></div></div>
  <div class="footer-band"><span>2240 Larch Street NW<br>Calgary, AB T2N 4K8</span><span>780.555.0142<br>780.555.0163</span><span>northgatecover.com<br>dreeve@northgatecover.com</span></div>
</section>

<!-- Envelope front -->
<section class="piece envelope envelope-front">
  <div class="wordmark wm-folder"><div class="mark-square"></div><div class="name"><b>Northgate</b><span>Insurance Brokers</span></div></div>
  <div class="return">dreeve@northgatecover.com<br>2240 Larch Street NW, Calgary, AB T2N 4K8</div>
  <div class="footer-band"></div>
</section>

<!-- Envelope back -->
<section class="piece envelope envelope-back">
  <svg class="flap" width="370" height="160" viewBox="0 0 370 160" aria-hidden="true">
    <path d="M0 0 L185 78 L370 0" fill="#ffffff" stroke="#d2d2d2" stroke-width="1"/>
    <path d="M0 160 L150 70 M370 160 L220 70" fill="none" stroke="#e2e2e2" stroke-width="1"/>
  </svg>
  <div class="seal"></div>
</section>
</body>
</html>
```